Gold Award for Hygiene Excellence

We are providing food safety consultancy to restaurant business in the uk. We would like to prepare an award sticker for business that work with us to get sticker award if they got 5 star hygiene rating consecutively in the their last 3 inspections. Normally, they display hygiene scores that are green color on their shop's window. So it should be catchy color for people easily detect the award. Size A5

```html
<!DOCTYPE html>
<html lang="en">
<head>
<meta charset="utf-8">
<title>Gold Award for Hygiene Excellence</title>
<link rel="stylesheet" href="https://fonts.googleapis.com/css2?family=Poppins:wght@500;600;700;800&display=swap">
<style>
  :root {
    --award-orange: #dc8428;
    --panel-white: #ffffff;
    --page-bg: #ffffff;
    --rating-green: #a6c72b;
    --text-grey: #7a7a7a;
    --brand-grey: #6f6f6f;
  }
  * { margin: 0; padding: 0; box-sizing: border-box; }
  html, body {
    width: 800px;
    height: 1200px;
    overflow: hidden;
    background: var(--page-bg);
  }
  body { font-family: "Poppins", Arial, sans-serif; }

  .award-sticker {
    position: absolute;
    left: 20px;
    top: 62px;
    width: 760px;
    height: 1075px;
    background: var(--award-orange);
  }

  .brand-panel {
    position: absolute;
    left: 183px;
    top: 0;
    width: 391px;
    height: 140px;
    background: var(--panel-white);
    display: flex;
    flex-direction: column;
    align-items: center;
    justify-content: center;
    color: var(--brand-grey);
    font-weight: 500;
    line-height: 1;
  }
  .brand-name {
    font-size: 50px;
    letter-spacing: 10px;
    margin-right: -10px;
  }
  .brand-descriptor {
    font-size: 22px;
    letter-spacing: 2px;
    margin-top: 10px;
  }

  .award-title {
    position: absolute;
    left: 0;
    width: 100%;
    text-align: center;
    color: var(--panel-white);
    font-weight: 700;
    line-height: 1;
  }
  .award-title--gold {
    top: 200px;
    font-size: 176px;
    letter-spacing: -4px;
  }
  .award-title--award {
    top: 380px;
    font-size: 122px;
    letter-spacing: -2px;
  }

  .dining-icon {
    position: absolute;
    left: 307px;
    top: 528px;
    width: 142px;
    height: 142px;
  }

  .award-subtitle {
    position: absolute;
    left: 0;
    top: 718px;
    width: 100%;
    text-align: center;
    color: var(--panel-white);
    font-size: 27px;
    font-weight: 500;
  }

  .rating-band {
    position: absolute;
    left: 0;
    top: 809px;
    width: 100%;
    height: 158px;
    background: var(--panel-white);
    display: flex;
    flex-direction: column;
    align-items: center;
  }
  .rating-row {
    display: flex;
    gap: 38px;
    margin-top: 26px;
  }
  .rating-badge {
    width: 44px;
    height: 44px;
    border: 4px solid var(--rating-green);
    border-radius: 50%;
    display: flex;
    align-items: center;
    justify-content: center;
    color: var(--text-grey);
    font-size: 24px;
    font-weight: 600;
    line-height: 1;
  }
  .rating-note {
    margin-top: 14px;
    text-align: center;
    color: var(--text-grey);
    font-size: 19px;
    font-weight: 600;
    line-height: 1.25;
  }
</style>
</head>
<body>
  <main class="award-sticker">
    <header class="brand-panel">
      <span class="brand-name">CARWEN</span>
      <span class="brand-descriptor">Food Safety Advisory</span>
    </header>

    <h1 class="award-title award-title--gold">GOLD</h1>
    <h2 class="award-title award-title--award">AWARD</h2>

    <svg class="dining-icon" viewBox="0 0 142 142" aria-hidden="true">
      <circle cx="71" cy="71" r="66" fill="none" stroke="#ffffff" stroke-width="7"/>
      <!-- fork -->
      <g fill="#ffffff">
        <rect x="48" y="30" width="4" height="30" rx="2"/>
        <rect x="56" y="30" width="4" height="30" rx="2"/>
        <rect x="64" y="30" width="4" height="30" rx="2"/>
        <path d="M47 56 h22 v4 c0 6 -4 9 -7 10 l1 42 c0 3 -2 5 -5 5 s-5 -2 -5 -5 l1 -42 c-3 -1 -7 -4 -7 -10 z"/>
        <!-- knife -->
        <path d="M84 28 c8 4 12 20 12 38 c0 6 -2 9 -5 10 l1 36 c0 3 -2 5 -5 5 s-5 -2 -5 -5 z"/>
      </g>
    </svg>

    <p class="award-subtitle">FOR HYGIENE EXCELLENCE</p>

    <section class="rating-band">
      <div class="rating-row">
        <span class="rating-badge">5</span>
        <span class="rating-badge">5</span>
        <span class="rating-badge">5</span>
      </div>
      <p class="rating-note">This award has been given for<br>3 consecutive 5 star hygiene score</p>
    </section>
  </main>
</body>
</html>
```